reminder mailer cards

redesign the reminder back cards , the cards are four to a standard sheet of card stock 8.5" x 11" expires 12/31/2020 replace ( across from meridale) with ( next to Penny Larder)

Font styles to use
Sans Serif

```html
<!DOCTYPE html>
<html lang="en">
<head>
<meta charset="utf-8">
<title>Rapid Lube – Reminder Card</title>
<link rel="stylesheet" href="https://fonts.googleapis.com/css2?family=Montserrat:wght@500;600;700;800;900&family=Kaushan+Script&display=swap">
<style>
  :root{
    --red:#e3172b;
    --red-dark:#a8101d;
    --blue:#1d4aa6;
    --blue-deep:#0d2a6e;
    --navy:#0a1a45;
    --white:#ffffff;
    --paper:#f2f2f2;
  }
  *{box-sizing:border-box;margin:0;padding:0}
  html,body{width:1200px;height:1200px;overflow:hidden;background:var(--paper)}
  body{position:relative;font-family:"Montserrat",sans-serif}
  .card{
    position:absolute;left:40px;top:167px;width:1082px;height:836px;
    background:var(--white);overflow:hidden;
    transform:scale(1.035);transform-origin:0 0;
    box-shadow:0 2px 10px rgba(0,0,0,.15);
  }
  .abs{position:absolute}

  /* top left headline */
  .headline{left:20px;top:36px;width:240px;text-align:center;color:var(--red);font-weight:900;line-height:1.02}
  .headline .l1{font-size:44px;letter-spacing:.5px;text-align:left;margin-left:4px}
  .headline .l2{font-size:30px}
  .headline .l3{font-size:44px}
  .service-list{left:30px;top:228px;width:214px;text-align:center;color:var(--blue);font-weight:600;font-size:22px;line-height:1.38;white-space:nowrap}
  .stopwatch{left:262px;top:18px;width:82px;height:70px}
  .mechanic{left:256px;top:100px;width:134px;height:240px;border-radius:40px;
    background:linear-gradient(180deg,#3b5fb0 0%,#2a4793 70%,#8a7a60 100%);opacity:.85}

  /* photo */
  .photo-wrap{left:390px;top:0;width:692px;height:362px}
  .badge{left:848px;top:0;width:168px;height:150px}
  .badge-text{left:848px;top:10px;width:168px;text-align:center;color:var(--white);font-weight:800;line-height:1.05}
  .badge-text .big{font-size:46px;font-weight:900}
  .badge-text .sm{font-size:29px}

  /* name band */
  .band{left:0;top:377px;width:1082px;height:180px}
  .brand-name{left:22px;top:400px;font-size:108px;line-height:1.1;font-weight:900;color:var(--red);letter-spacing:5px;white-space:nowrap}
  .tire-track{left:868px;top:378px;width:214px;height:152px;background:linear-gradient(135deg,#e3172b 0%,#f04a57 100%);opacity:.9;
    clip-path:polygon(8% 55%,30% 5%,100% 0,100% 100%,20% 100%)}

  .address{left:26px;top:562px;font-family:"Kaushan Script",cursive;font-size:46px;letter-spacing:1.5px;color:var(--blue);white-space:nowrap}

  /* bottom */
  .bottom{left:0;top:640px;width:1082px;height:196px;background:var(--blue)}
  .hours-title{left:72px;top:654px;color:var(--white);font-size:28px;font-weight:800;display:flex;align-items:center;gap:10px}
  .hours{left:24px;top:690px;width:330px;text-align:center;color:var(--white);font-size:24px;font-weight:700;line-height:1.35}
  .call-bar{left:0;top:766px;width:412px;height:70px}
  .call-text{left:24px;top:786px;color:var(--white);font-size:26px;font-weight:600;letter-spacing:1px;white-space:nowrap}
  .call-text .num{font-size:21px;font-weight:700;margin-left:14px;letter-spacing:.5px}

  .coupon{left:420px;top:660px;width:634px;height:160px}
  .coupon-title{left:500px;top:668px;font-family:"Kaushan Script",cursive;font-size:50px;color:var(--white)}
  .coupon-save{left:450px;top:752px;color:var(--white);font-size:34px;font-weight:700}
  .coupon-save b{font-weight:800}
  .coupon-detail{left:660px;top:754px;color:var(--white);font-size:17px;font-weight:700;line-height:1.3;text-align:center}
  .coupon-side{left:880px;top:680px;width:136px;text-align:center;color:var(--white);line-height:1.2}
  .coupon-side .note{font-size:16px;font-weight:600}
  .coupon-side .exp{font-size:21px;font-weight:700;margin-top:10px}
</style>
</head>
<body>
<div class="card">

  <div class="abs headline">
    <div class="l1">IT'S TIME</div>
    <div class="l2">FOR</div>
    <div class="l3">RAPID</div>
    <div class="l3">LUBE!</div>
  </div>
  <svg class="abs stopwatch" viewBox="0 0 82 70" aria-hidden="true">
    <g fill="none" stroke="#1d4aa6" stroke-width="3.5" stroke-linecap="round">
      <circle cx="48" cy="40" r="24"/>
      <path d="M44 10h8M48 10v6M48 40V26M48 40l9 6"/>
      <path d="M4 32h14M8 40h10M4 48h14"/>
    </g>
  </svg>
  <div class="abs service-list">9MINUTE<br>14POINT<br>OIL AND LUBE<br>SERVICE</div>
  <div class="abs mechanic" role="img" aria-label="Cartoon mechanic in blue overalls carrying a large wrench over his shoulder"></div>

  <svg class="abs photo-wrap" viewBox="0 0 692 362" preserveAspectRatio="none">
    <defs>
      <linearGradient id="photoGrad" x1="0" y1="0" x2="0" y2="1">
        <stop offset="0" stop-color="#5f8a4a"/>
        <stop offset=".4" stop-color="#8fa87e"/>
        <stop offset=".55" stop-color="#c44a5a"/>
        <stop offset=".7" stop-color="#3f62b0"/>
        <stop offset=".85" stop-color="#6d6d72"/>
        <stop offset="1" stop-color="#5a5a5f"/>
      </linearGradient>
    </defs>
    <polygon points="108,0 692,0 692,362 2,362" fill="#1d4aa6"/>
    <g role="img" aria-label="Red, white and blue race car speeding along a track">
      <polygon points="122,0 692,0 692,362 22,362" fill="url(#photoGrad)"/>
    </g>
  </svg>

  <svg class="abs badge" viewBox="0 0 168 150" aria-hidden="true">
    <polygon points="0,0 168,0 168,125 84,150 0,125" fill="#e3172b"/>
    <polygon points="0,0 168,0 168,125 84,150 0,125" fill="none" stroke="#a8101d" stroke-width="3"/>
  </svg>
  <div class="abs badge-text">
    <div class="big">FREE</div>
    <div class="sm">Vacuum</div>
    <div class="sm">Mon-Fri</div>
  </div>

  <svg class="abs band" viewBox="0 0 1082 180" aria-hidden="true">
    <defs>
      <linearGradient id="bandGrad" x1="0" y1="0" x2="0" y2="1">
        <stop offset="0" stop-color="#0a1a45"/>
        <stop offset=".5" stop-color="#17367f"/>
        <stop offset="1" stop-color="#0a1a45"/>
      </linearGradient>
    </defs>
    <polygon points="0,0 900,0 812,160 0,160" fill="url(#bandGrad)"/>
    <polygon points="0,163 276,163 268,178 0,178" fill="#e3172b"/>
    <polygon points="284,163 500,163 492,178 276,178" fill="#1d4aa6"/>
    <polygon points="508,163 808,163 800,178 500,178" fill="#e3172b"/>
  </svg>
  <div class="abs brand-name">RAPID LUBE</div>
  <div class="abs tire-track" role="img" aria-label="Red tire tread mark"></div>

  <div class="abs address">48 Marlow Road Ashby ( next to Penny Larder )</div>

  <div class="abs bottom"></div>
  <div class="abs hours-title">
    <svg width="32" height="32" viewBox="0 0 32 32" aria-hidden="true">
      <circle cx="16" cy="16" r="13" fill="none" stroke="#fff" stroke-width="3"/>
      <path d="M16 8v8l6 4" fill="none" stroke="#fff" stroke-width="3" stroke-linecap="round"/>
    </svg>
    Hours:
  </div>
  <div class="abs hours">Mon-Fri 8Am-5:00 Pm,<br>Sat 8Am-3Pm</div>

  <svg class="abs call-bar" viewBox="0 0 412 70" aria-hidden="true">
    <defs>
      <linearGradient id="callGrad" x1="0" y1="0" x2="1" y2="0">
        <stop offset="0" stop-color="#a8101d"/>
        <stop offset=".5" stop-color="#e3172b"/>
        <stop offset="1" stop-color="#a8101d"/>
      </linearGradient>
    </defs>
    <polygon points="0,0 412,0 370,70 0,70" fill="url(#callGrad)"/>
  </svg>
  <div class="abs call-text">CALL US<span class="num">1.555-014-2290</span></div>

  <svg class="abs coupon" viewBox="0 0 634 160" aria-hidden="true">
    <defs>
      <linearGradient id="couponGrad" x1="0" y1="0" x2="1" y2="1">
        <stop offset="0" stop-color="#a8101d"/>
        <stop offset=".5" stop-color="#e3172b"/>
        <stop offset="1" stop-color="#a8101d"/>
      </linearGradient>
    </defs>
    <polygon points="0,0 634,0 610,80 634,160 0,160" fill="url(#couponGrad)"/>
    <polygon points="12,10 614,10 592,80 612,150 12,150" fill="none" stroke="#fff" stroke-width="2" stroke-dasharray="8 6"/>
    <line x1="458" y1="22" x2="458" y2="140" stroke="#fff" stroke-width="2"/>
  </svg>
  <div class="abs coupon-title">Express Lube</div>
  <div class="abs coupon-save">Save <b>$5.00</b></div>
  <div class="abs coupon-detail">9MINUTE 14POINT<br>COMPLETE SERVICE</div>
  <div class="abs coupon-side">
    <div class="note">with<br>this<br>cupon</div>
    <div class="exp">EXPIRES<br>12/31/2020</div>
  </div>

</div>
</body>
</html>
```